Business Card Design

We need a business card design for an existing business. Our main trading brand is www.brightquillsaver.co.uk

We attach various logo files - please use the version that will produce the sharpest image on the business card.

We are flexible about shape of card etc. Please think outside the box as to what goes on front and what goes on back of the card

We want to be able to amend the card (once the design has been agreed ) to add additional staff details, but the text to go on it will be generic

Details to go on card ( for the first generic one) are fairly minimal as we don't like cluttered business cards:-

Neil Cathcart
Managing Director

Mobile: 07841 258 407
Email: n.cathcart@brightquillsaver.co.uk

Industry/Entity Type

Business

```html
<!DOCTYPE html>
<html lang="en">
<head>
<meta charset="utf-8">
<title>Bright Quill Saver – Business Card</title>
<link href="https://fonts.googleapis.com/css2?family=Montserrat:wght@300;700&family=Quicksand:wght@400&display=swap" rel="stylesheet">
<style>
  :root {
    --page-bg: #d6d8db;
    --card-top: #303236;
    --card-bottom: #1f2023;
    --ice: #b4c6d6;
    --ice-blue: #6e9dc8;
    --brand: #7ea6cc;
    --text-light: #e4e7ea;
    --text-muted: #9aa2ab;
    --badge: #c9ccd0;
  }
  * { margin: 0; padding: 0; box-sizing: border-box; }
  html, body { width: 1200px; height: 900px; overflow: hidden; }
  body {
    background: var(--page-bg);
    display: flex;
    flex-direction: column;
    align-items: center;
    justify-content: center;
    gap: 60px;
  }
  .card {
    position: relative;
    width: 560px;
    height: 362px;
    border-radius: 4px;
    overflow: hidden;
    background: linear-gradient(160deg, var(--card-top), var(--card-bottom));
    box-shadow: 0 10px 30px rgba(0,0,0,.25);
  }
  .card__accent {
    position: absolute;
    right: 0;
    bottom: 0;
    width: 300px;
    height: 150px;
    background: linear-gradient(135deg, rgba(180,198,214,0) 35%, rgba(180,198,214,.28) 70%, rgba(110,157,200,.55));
    clip-path: polygon(100% 0, 100% 100%, 0 100%);
  }
  .card__rule {
    position: absolute;
    left: 0;
    right: 0;
    bottom: 0;
    height: 6px;
    background: var(--ice-blue);
  }
  .identity {
    position: absolute;
    top: 44px;
    left: 170px;
    display: flex;
    align-items: center;
    gap: 12px;
  }
  .identity__badge { width: 62px; height: 26px; background: var(--badge); }
  .identity__divider { width: 1px; height: 34px; background: var(--text-muted); }
  .identity__name {
    font-family: "Montserrat", sans-serif;
    font-weight: 700;
    font-size: 17px;
    letter-spacing: .5px;
    color: var(--text-light);
    text-transform: uppercase;
    line-height: 1.1;
  }
  .identity__role {
    font-family: "Montserrat", sans-serif;
    font-weight: 300;
    font-size: 11px;
    letter-spacing: 1px;
    color: var(--text-muted);
    text-transform: uppercase;
  }
  .contact {
    position: absolute;
    top: 112px;
    left: 170px;
    list-style: none;
    font-family: "Quicksand", sans-serif;
    font-size: 11px;
    color: var(--text-muted);
  }
  .contact__item { display: flex; align-items: center; gap: 12px; margin-bottom: 10px; }
  .contact__icon {
    width: 16px; height: 16px;
    background: var(--ice-blue);
    border-radius: 2px;
    display: flex; align-items: center; justify-content: center;
  }
  .wordmark {
    position: absolute;
    font-family: "Quicksand", sans-serif;
    font-weight: 400;
    color: var(--brand);
    white-space: nowrap;
  }
  .card--front .wordmark { left: 26px; bottom: 90px; font-size: 30px; }
  .card--back .wordmark { left: 36px; top: 120px; font-size: 40px; }
</style>
</head>
<body>

<section class="card card--front" aria-label="Card front">
  <div class="card__accent"></div>
  <div class="card__rule"></div>

  <div class="identity">
    <span class="identity__badge"></span>
    <span class="identity__divider"></span>
    <div>
      <p class="identity__name">Neil Cathcart</p>
      <p class="identity__role">Managing Director</p>
    </div>
  </div>

  <ul class="contact">
    <li class="contact__item">
      <span class="contact__icon">
        <svg width="10" height="10" viewBox="0 0 24 24" aria-hidden="true"><path fill="#fff" d="M6.6 10.8a15.1 15.1 0 0 0 6.6 6.6l2.2-2.2a1 1 0 0 1 1-.25 11.4 11.4 0 0 0 3.6.57 1 1 0 0 1 1 1V20a1 1 0 0 1-1 1A17 17 0 0 1 3 4a1 1 0 0 1 1-1h3.5a1 1 0 0 1 1 1c0 1.25.2 2.45.57 3.57a1 1 0 0 1-.25 1z"/></svg>
      </span>
      <span>07841 258 407</span>
    </li>
    <li class="contact__item">
      <span class="contact__icon">
        <svg width="10" height="10" viewBox="0 0 24 24" aria-hidden="true"><rect x="2" y="5" width="20" height="14" rx="1" fill="#fff"/><path d="M2 6l10 7 10-7" fill="none" stroke="#6e9dc8" stroke-width="2"/></svg>
      </span>
      <span>n.cathcart@brightquillsaver.co.uk</span>
    </li>
  </ul>

  <p class="wordmark">brightquillsaver.co.uk</p>
</section>

<section class="card card--back" aria-label="Card back">
  <div class="card__accent"></div>
  <div class="card__rule"></div>
  <p class="wordmark">brightquillsaver.co.uk</p>
</section>

</body>
</html>
```